Verdant Medispa Business Card

need a business card for our medispa, attached please see the logo.
our website is https://verdantmedispa-example.com

Sorina Belcourt, MD
Internal Medicine

555-204-7193

Sorina@verdantmedispa-example.com

Www.Verdantmedispa-example.com

738 E Harlow Blvd N, Ste 512, Katy, TX 77981

Target Market(s)

MedSpa, Cosmetics, Esthetics

Industry/Entity Type

MedicalSpa

Contact Information for Business Card

Please see the attached business card which i pulled from the internet. I like the idea back as a logo and front with info.

Font styles to use
Decorative

Requirements
Must have
• Color should be matching with Logo and Website theme, Also I like to have QR code for the website

```html
<!DOCTYPE html>
<html lang="en">
<head>
<meta charset="utf-8">
<title>Verdant Medispa Business Card</title>
<link rel="stylesheet" href="https://fonts.googleapis.com/css2?family=Figtree:wght@400;500&display=swap">
<style>
  :root {
    --stage: #b0b0b0;
    --card: #1e1510;
    --gold: #d9a47e;
    --ink: #ffffff;
  }
  html, body {
    margin: 0;
    padding: 0;
    width: 1200px;
    height: 1039px;
    overflow: hidden;
    background: var(--stage);
    font-family: "Figtree", Arial, sans-serif;
  }
  .stage {
    position: relative;
    width: 1200px;
    height: 1039px;
  }
  .card {
    position: absolute;
    left: 315px;
    width: 571px;
    height: 327px;
    border-radius: 12px;
    background: var(--card);
  }
  .card-front { top: 160px; }
  .card-back { top: 554px; }
  .wordmark {
    position: absolute;
    margin: 0;
    color: var(--gold);
    font-weight: 400;
    white-space: nowrap;
    letter-spacing: 0.5px;
  }
  .card-front .wordmark {
    left: 0;
    right: 0;
    top: 142px;
    text-align: center;
    font-size: 38px;
    line-height: 44px;
  }
  .card-back .wordmark {
    left: 45px;
    top: 48px;
    font-size: 22px;
    line-height: 28px;
  }
  .address,
  .contact {
    position: absolute;
    left: 304px;
    margin: 0;
    color: var(--ink);
    font-size: 13px;
    line-height: 16.5px;
    font-style: normal;
  }
  .address { top: 47px; }
  .contact { top: 242px; }
  .person {
    position: absolute;
    left: 45px;
    top: 241px;
    color: var(--ink);
  }
  .person-name {
    margin: 0;
    font-size: 21px;
    line-height: 26px;
    font-weight: 400;
  }
  .person-title {
    margin: 0;
    font-size: 16px;
    line-height: 20px;
  }
</style>
</head>
<body>
<main class="stage">
  <section class="card card-front" aria-label="Card front">
    <p class="wordmark">Verdant MediSpa</p>
  </section>

  <section class="card card-back" aria-label="Card back">
    <p class="wordmark">Verdant MediSpa</p>
    <address class="address">738 E Harlow Blvd N,<br>Ste 512, Katy, TX 77981</address>
    <div class="person">
      <h1 class="person-name">Sorina Belcourt, MD</h1>
      <p class="person-title">Internal Medicine</p>
    </div>
    <p class="contact">
      P: 555-204-7193<br>
      E: Sorina@verdantmedispa-example.com<br>
      W: www.Verdantmedispa-example.com
    </p>
  </section>
</main>
</body>
</html>
```